Business Card Design

I am a classical pilates instructor. I have a home studio, teach out a of a large studio downtown, and teach at on location corporate settings
I like my card to be very simple and clean.
I would like a silhouette of the picture I'm uploading on my design. In the upload section it looks like the picture is cut off and only showing a leg in the air...let me know if you can open up the entire picture.

Industry/Entity Type
Business
Contact Information for Business Card
Norah Fennick Pilates
Certified - The Pilates Hall of Marrow Creek
nf.fennick27@quillpost.example
555.314.7720

```html
<!DOCTYPE html>
<html lang="en">
<head>
<meta charset="utf-8">
<title>Norah Fennick Pilates – Business Card</title>
<link rel="stylesheet" href="https://fonts.googleapis.com/css2?family=Comfortaa:wght@500;600&display=swap">
<style>
  :root {
    --paper: #ffffff;
    --ink-navy: #2b2d8c;
    --band-green: #b3e597;
    --band-blue: #cad7f8;
    --band-lime-pale: #d4fb95;
    --hill-green: #62906f;
    --hill-green-deep: #4f7a60;
    --rule-lime: #8ef000;
    --rule-blue: #7b9cf0;
    --figure-lime: #99ff00;
    --figure-lime-soft: #c4ff6e;
    --contact-white: #ffffff;
  }
  html, body {
    margin: 0;
    padding: 0;
    width: 1200px;
    height: 702px;
    overflow: hidden;
    background: var(--paper);
  }
  .business-card {
    display: block;
    width: 1200px;
    height: 702px;
  }
  .card-text {
    font-family: "Comfortaa", "Quicksand", sans-serif;
    font-weight: 600;
    text-anchor: end;
  }
  .card-name { fill: var(--ink-navy); font-size: 52px; letter-spacing: -1px; }
  .card-credential { fill: var(--ink-navy); font-size: 40px; letter-spacing: -1px; }
  .card-studio { fill: var(--ink-navy); font-size: 29px; letter-spacing: -1px; }
  .card-email { fill: var(--contact-white); font-size: 32px; font-weight: 600; letter-spacing: -1px; }
  .card-phone { fill: var(--contact-white); font-size: 40px; font-weight: 600; letter-spacing: 0.5px; }
  .band-green { fill: var(--band-green); }
  .band-blue { fill: var(--band-blue); }
  .band-lime-pale { fill: var(--band-lime-pale); }
  .hill-green { fill: var(--hill-green); }
  .hill-green-deep { fill: var(--hill-green-deep); }
  .hill-navy { fill: var(--ink-navy); }
  .rule-lime { stroke: var(--rule-lime); stroke-width: 7; }
  .rule-blue { stroke: var(--rule-blue); stroke-width: 7; }
  .figure-area { fill: url(#figure-fill); }
</style>
</head>
<body>
<svg class="business-card" viewBox="0 0 1085 635" width="1200" height="702" xmlns="http://www.w3.org/2000/svg">
  <defs>
    <linearGradient id="figure-fill" x1="0" y1="0" x2="0" y2="1">
      <stop offset="0" stop-color="var(--figure-lime-soft)"/>
      <stop offset="1" stop-color="var(--figure-lime)"/>
    </linearGradient>
  </defs>

  <rect width="1085" height="635" fill="var(--paper)"/>

  <g class="background-bands">
    <polygon class="band-green" points="615,0 1085,0 1085,635 320,635"/>
    <polygon class="band-blue" points="365,0 615,0 458,345"/>
    <polygon class="band-lime-pale" points="458,345 508,520 352,575"/>
  </g>

  <g class="background-hill">
    <path class="hill-green" d="M352,575 Q760,470 1085,185 L1085,635 L320,635 Z"/>
    <polygon class="hill-green-deep" points="352,575 508,528 538,635 320,635"/>
    <path class="hill-navy" d="M0,625 Q180,585 352,575 L320,635 L0,635 Z"/>
  </g>

  <g class="header-rules">
    <line class="rule-lime" x1="375" y1="141" x2="1085" y2="141"/>
    <line class="rule-blue" x1="441" y1="158" x2="1085" y2="158"/>
  </g>

  <rect class="figure-area" x="55" y="50" width="295" height="495" rx="14"
        role="img" aria-label="Silhouette of a pilates instructor in a leg-raised pose"/>

  <g class="card-text">
    <text class="card-name" x="1025" y="112">norah fennick</text>
    <text class="card-credential" x="1022" y="210">pilates certified</text>
    <text class="card-studio" x="1028" y="260">the pilates hall of marrow creek</text>
    <text class="card-email" x="1010" y="495">nf.fennick27@quillpost.example</text>
    <text class="card-phone" x="1005" y="558">555 314 7720</text>
  </g>
</svg>
</body>
</html>
```